Faithful in the Small...Powerful together

Capital Campaign for Brightwell Chapel...need it engaging..spiritually based with pics of the community etc...

Target Market(s)

church congregation and sphere of influence

Industry/Entity Type

religious

Colors
EB3D1F
EC4F4E
F09395
F8D3D4
FCEDEE

Requirements
Must have
• tier levels..engaging scripture and photos

```html
<!DOCTYPE html>
<html lang="en">
<head>
<meta charset="utf-8">
<title>Faithful in the Small, Powerful Together – Brightwell Chapel Capital Campaign</title>
<link href="https://fonts.googleapis.com/css2?family=Montserrat:wght@400;500;600;700&family=Dancing+Script:wght@500;700&display=swap" rel="stylesheet">
<style>
  :root{
    --red:#EB3D1F;
    --red-soft:#EC4F4E;
    --pink:#F09395;
    --pink-light:#F8D3D4;
    --pink-pale:#FCEDEE;
    --ink:#1d1d1d;
    --black:#111111;
    --white:#ffffff;
    --stage:#ffffff;
  }
  *{box-sizing:border-box;margin:0;padding:0}
  html,body{width:1200px;height:456px;overflow:hidden;background:var(--stage)}
  body{font-family:"Montserrat",sans-serif;color:var(--ink);position:relative}

  .sheet-slot{position:absolute;top:18px;width:297px;height:420px}
  .sheet-slot--front{left:283px}
  .sheet-slot--back{left:620px}
  .sheet{position:absolute;left:0;top:0;width:590px;height:834px;background:var(--white);
    transform:scale(.5036);transform-origin:0 0;overflow:hidden;box-shadow:0 2px 8px rgba(0,0,0,.18)}

  /* ---------- front ---------- */
  .hero{position:absolute;left:0;top:0;width:590px;height:520px}
  .hero__tagline{font-family:"Dancing Script",cursive;font-weight:700;font-size:40px}
  .brand{position:absolute;left:26px;top:100px;line-height:1}
  .brand__name{font-size:40px;font-weight:700;color:var(--ink);letter-spacing:-.5px}
  .brand__sub{font-size:19px;font-weight:600;color:var(--ink);margin-top:6px;margin-left:60px;letter-spacing:1px}

  .goal-pill{position:absolute;left:138px;top:455px;height:36px;display:flex;font-size:20px;font-weight:600;color:var(--white);border-radius:3px;overflow:hidden}
  .goal-pill__label{background:var(--pink);color:var(--ink);padding:6px 10px;font-weight:700}
  .goal-pill__value{background:var(--red);padding:6px 12px}
  .goal-pill__value b{font-weight:700}

  .facts{position:absolute;left:28px;top:512px;width:537px;height:76px;border:2px solid var(--pink-light);display:flex}
  .facts__list{flex:1;padding:13px 0 0 26px;font-size:12.5px;line-height:16px}
  .facts__list b{font-weight:700}
  .accent{color:var(--red)}
  .facts__list .accent{font-weight:700}
  .facts__avg{width:220px;background:var(--pink-pale);padding:22px 0 0 30px;font-size:12.5px;line-height:14px}
  .facts__avg .accent{font-weight:700}

  .vision-title{position:absolute;left:0;width:590px;top:600px;text-align:center;font-size:21px;font-weight:700;color:var(--red)}
  .vision-bar{position:absolute;left:52px;top:638px;width:510px;height:28px;display:flex;font-size:12.5px;font-weight:500;white-space:nowrap}
  .vision-bar span{padding:6px 18px}
  .vision-bar span:first-child{background:var(--pink-light)}
  .vision-bar span:last-child{background:var(--pink-pale);flex:1}

  .motto{position:absolute;left:82px;top:676px;font-family:"Dancing Script",cursive;font-weight:500;font-size:30px;line-height:32px;color:var(--red-soft)}
  .scripture{position:absolute;left:266px;top:688px;width:260px;font-size:12px;line-height:16px}
  .scripture p{padding-bottom:6px}
  .scripture p+p{border-top:1.5px solid var(--red);padding-top:8px}
  .scripture cite{font-style:normal;font-weight:700;color:var(--red)}

  .footer{position:absolute;left:0;bottom:0;width:590px;height:44px;background:var(--red);display:flex;align-items:center;justify-content:center;gap:40px;color:var(--white)}
  .footer__phone{font-size:19px;font-weight:700;display:flex;align-items:center;gap:10px}
  .footer__web{font-size:12.5px;display:flex;align-items:center;gap:8px}

  /* ---------- back ---------- */
  .stories{position:absolute;left:0;top:0;width:392px;height:305px;background:var(--pink-light);border-bottom-right-radius:48px;z-index:2;padding:22px 26px 0 27px}
  .stories__head{position:absolute;left:0;top:0;width:392px;height:62px;background:var(--pink-pale)}
  .stories h2{position:relative;font-size:21px;font-weight:700;color:var(--red);margin-bottom:26px}
  .stories p{position:relative;font-size:11.5px;line-height:14.4px;margin-bottom:14px;width:340px}
  .stage-photo{position:absolute;left:360px;top:0;width:230px;height:305px}

  .section-title{font-size:21px;font-weight:700;color:var(--red);line-height:20px}
  .forward{position:absolute;left:0;top:305px;width:296px;height:175px;background:var(--pink-pale);padding:16px 0 0 27px}
  .forward h3{font-size:11.5px;font-weight:700;margin:20px 0 18px}
  .forward p{font-size:11.5px;line-height:14.4px;width:250px}

  .commitment{position:absolute;left:0;top:480px;width:296px;height:165px;background:#2b2b2b;padding:10px 0 0 27px;color:var(--white)}
  .commitment p{font-size:11.5px;line-height:14.4px;width:250px;margin-top:12px}

  .join{position:absolute;left:27px;top:655px;width:260px}
  .join ul{list-style:none;margin:12px 0 10px;font-size:11.5px;font-weight:700;line-height:17px}
  .join li::before{content:"";display:inline-block;width:5px;height:5px;background:var(--red);margin-right:6px;vertical-align:2px}
  .join p{font-size:11.5px;line-height:14.4px}

  .model{position:absolute;left:324px;top:320px;width:250px}
  .model__intro{font-size:11.5px;line-height:14.4px;margin:14px 0 16px}
  .model__label{font-size:11.5px;font-weight:700;margin-bottom:10px}
  .tiers{border-collapse:collapse;width:242px;font-size:9.5px;text-align:center}
  .tiers th,.tiers td{border:1.5px solid var(--pink-light)}
  .tiers th{font-size:11px;font-weight:700;height:44px;line-height:12px}
  .tiers td{height:44px}
  .tiers td:first-child{text-align:left;padding-left:6px;font-size:8.5px;line-height:10px}
  .total{margin-top:22px;font-size:21px;font-weight:700}
  .total__note{font-size:11.5px;margin:2px 0 10px}
  .model ul{list-style:none;font-size:11.5px;font-weight:700;line-height:16.5px}
  .model li::before{content:"";display:inline-block;width:5px;height:5px;background:var(--red);margin-right:6px;vertical-align:2px}
</style>
</head>
<body>

<div class="sheet-slot sheet-slot--front">
  <article class="sheet">
    <svg class="hero" viewBox="0 0 590 520" width="590" height="520">
      <defs>
        <linearGradient id="pastorTone" x1="0" y1="0" x2="1" y2="1">
          <stop offset="0" stop-color="#c9433a"/>
          <stop offset=".5" stop-color="#7b5a66"/>
          <stop offset="1" stop-color="#3a2e35"/>
        </linearGradient>
        <linearGradient id="crowdTone" x1="0" y1="0" x2="1" y2="1">
          <stop offset="0" stop-color="#a88a80"/>
          <stop offset=".6" stop-color="#c8453d"/>
          <stop offset="1" stop-color="#5b4a4c"/>
        </linearGradient>
        <linearGradient id="fadeWhite" x1="0" y1="0" x2="0" y2="1">
          <stop offset="0" stop-color="#fff" stop-opacity="0"/>
          <stop offset="1" stop-color="#fff" stop-opacity="1"/>
        </linearGradient>
        <path id="taglineCurve" d="M18 452 Q330 446 578 228"/>
      </defs>
      <rect x="0" y="0" width="590" height="480" fill="url(#pastorTone)" role="img" aria-label="Photo of the pastor preaching with open hands"/>
      <rect x="0" y="240" width="300" height="190" fill="url(#crowdTone)" role="img" aria-label="Photo of congregation members praying together"/>
      <rect x="0" y="450" width="590" height="70" fill="url(#fadeWhite)"/>
      <path d="M0 0 H330 C350 90 310 190 220 222 C150 245 70 245 0 240 Z" fill="#fff"/>
      <path d="M0 398 Q330 395 590 185 L590 250 Q360 470 0 472 Z" fill="var(--black)"/>
      <path d="M0 398 Q330 395 590 185" fill="none" stroke="var(--red)" stroke-width="3"/>
      <path d="M0 472 Q360 470 590 250 L590 258 Q360 480 0 480 Z" fill="#fff"/>
      <text class="hero__tagline" fill="#fff">
        <textPath href="#taglineCurve" textLength="610" lengthAdjust="spacingAndGlyphs">Faithful in the Small, <tspan fill="var(--red)">Powerful Together.</tspan></textPath>
      </text>
    </svg>

    <div class="brand">
      <div class="brand__name">Brightwell</div>
      <div class="brand__sub">CHAPEL</div>
    </div>

    <div class="goal-pill">
      <span class="goal-pill__label">Goal:</span>
      <span class="goal-pill__value"><b>$150,000</b>&nbsp;in <b>12</b> Months</span>
    </div>

    <div class="facts">
      <div class="facts__list">
        <div><b>Total Goal:</b> <span class="accent">$150,000</span></div>
        <div><b>Active Members:</b> approximately <span class="accent">150</span> people</div>
        <div><b>Timeframe:</b> <span class="accent">12</span> months</div>
      </div>
      <div class="facts__avg">That is <span class="accent">$1,000</span> per person<br>per year on average</div>
    </div>

    <h2 class="vision-title">The Heart of the Vision</h2>
    <div class="vision-bar">
      <span>We are restoring more than space</span>
      <span>We are restoring a church where we</span>
    </div>

    <div class="motto">Love like Him<br>Live like Him<br>Lead like Him</div>

    <div class="scripture">
      <p>“Whoever is faithful in very little is also faithful in much.” <cite>Luke 16:10</cite></p>
      <p>“How good and pleasant it is when God’s people live together in unity.” <cite>Psalm 133:1</cite></p>
    </div>

    <footer class="footer">
      <span class="footer__phone">
        <svg width="20" height="20" viewBox="0 0 24 24" aria-hidden="true"><path fill="#fff" d="M6.6 10.8a15 15 0 0 0 6.6 6.6l2.2-2.2c.3-.3.7-.4 1-.2 1.1.4 2.3.6 3.6.6.6 0 1 .4 1 1V20c0 .6-.4 1-1 1A17 17 0 0 1 3 4c0-.6.4-1 1-1h3.5c.6 0 1 .4 1 1 0 1.3.2 2.5.6 3.6.1.3 0 .7-.2 1z"/></svg>
        555.014.2290
      </span>
      <span class="footer__web">
        <svg width="14" height="14" viewBox="0 0 24 24" aria-hidden="true"><circle cx="12" cy="12" r="10" fill="none" stroke="#fff" stroke-width="2"/><path d="M2 12h20M12 2c3 3 3 17 0 20M12 2c-3 3-3 17 0 20" fill="none" stroke="#fff" stroke-width="1.5"/></svg>
        www.brightwell-chapel.org
      </span>
    </footer>
  </article>
</div>

<div class="sheet-slot sheet-slot--back">
  <article class="sheet">
    <section class="stories">
      <div class="stories__head"></div>
      <h2>Stories of What God Is Doing</h2>
      <p>One Wednesday night, a woman went to visit another church, but they were closed for a break. Instead of turning back, she came here. That unexpected moment became a divine appointment. God brought her to Brightwell.</p>
      <p>Another couple walked through our doors carrying deep church hurt. From the very first moment, they felt seen, valued, and welcomed. What they found here was not just a service, but a family.</p>
      <p>This is what we are building together.</p>
      <p>These gifts help build momentum, inspire others, and move the vision forward in powerful ways.</p>
    </section>
    <div class="stage-photo" role="img" aria-label="Photo of a worship leader singing on a dark stage" style="background:linear-gradient(160deg,#3a2a24 0%,#141414 45%,#1f5a4a 75%,#111 100%)"></div>

    <section class="forward">
      <h2 class="section-title">How We Move<br>Forward Together</h2>
      <h3>We encourage</h3>
      <p>Everyone to participate, even one dollar a day matters Some to give stretch gifts as they are able A few to provide leadership gifts to help anchor the campaign</p>
    </section>

    <section class="commitment">
      <h2 class="section-title">A Shared<br>Commitment</h2>
      <p>“If each of us gave just $20 a week, we would not only meet our goal, we would exceed it. But this is not about equal giving. It is about equal sacrifice. Some can give more, some less, but together, we can do something powerful.”</p>
    </section>

    <section class="join">
      <h2 class="section-title">Join Us</h2>
      <ul><li>Pray</li><li>Listen</li><li>Step forward in faith</li></ul>
      <p>Together, we believe God will do more than we can ask or imagine.</p>
    </section>

    <section class="model">
      <h2 class="section-title">Realistic<br>Participation Model</h2>
      <p class="model__intro">Not everyone will give equally<br>so let’s build a real-world scenario:</p>
      <p class="model__label">Tiered Giving Plan</p>
      <table class="tiers">
        <thead><tr><th>Group</th><th>People</th><th>Weekly<br>Gift</th><th>Yearly<br>Total</th></tr></thead>
        <tbody>
          <tr><td>Leadership<br>Givers</td><td>10</td><td>$100</td><td>$52,000</td></tr>
          <tr><td>Core<br>Givers</td><td>40</td><td>$40</td><td>$38,200</td></tr>
          <tr><td>Consistent<br>Givers</td><td>60</td><td>$20</td><td>$62,400</td></tr>
          <tr><td>Entry<br>Givers</td><td>40</td><td>$10</td><td>$20,800</td></tr>
        </tbody>
      </table>
      <p class="total">Total: <span class="accent">$218,400</span></p>
      <p class="total__note">This exceeds the goal, giving margin for:</p>
      <ul><li>Missed weeks</li><li>Lower participation</li><li>Unexpected needs</li></ul>
    </section>

    <footer class="footer">
      <span class="footer__phone">
        <svg width="20" height="20" viewBox="0 0 24 24" aria-hidden="true"><path fill="#fff" d="M6.6 10.8a15 15 0 0 0 6.6 6.6l2.2-2.2c.3-.3.7-.4 1-.2 1.1.4 2.3.6 3.6.6.6 0 1 .4 1 1V20c0 .6-.4 1-1 1A17 17 0 0 1 3 4c0-.6.4-1 1-1h3.5c.6 0 1 .4 1 1 0 1.3.2 2.5.6 3.6.1.3 0 .7-.2 1z"/></svg>
        555.014.2290
      </span>
      <span class="footer__web">
        <svg width="14" height="14" viewBox="0 0 24 24" aria-hidden="true"><circle cx="12" cy="12" r="10" fill="none" stroke="#fff" stroke-width="2"/><path d="M2 12h20M12 2c3 3 3 17 0 20M12 2c-3 3-3 17 0 20" fill="none" stroke="#fff" stroke-width="1.5"/></svg>
        www.brightwell-chapel.org
      </span>
    </footer>
  </article>
</div>

</body>
</html>
```